Website Falcrest Trail

Hi I'm looking for a simple design for a new website. It's outdoor products mainly in category, Boat, Tarpaulin, Fishing, Golf. I have include image and text for 8 products + presentation etc. I want a simple and modern site + fast + Mobile. Wordpress. I'm going to sell through Velmora so I don't need any WooCommerce but a buy button to Velmora. I haven set up the Velmora account yet. My logo i s grey and orange. My goal is to sell in Velmora US and later EU.

```html
<!DOCTYPE html>
<html lang="en">
<head>
<meta charset="utf-8">
<title>Falcrest Trail</title>
<link href="https://fonts.googleapis.com/css2?family=Montserrat:wght@500;600;700;800;900&family=Roboto:wght@300;400;500&display=swap" rel="stylesheet">
<style>
:root{
  --orange:#f7941d;
  --ink:#333333;
  --grey-text:#6f6f6f;
  --muted:#9a9a9a;
  --band:#ebebeb;
  --footer:#3a3a3a;
  --white:#ffffff;
  --peach:#efd3b3;
}
*{box-sizing:border-box;margin:0;padding:0}
html,body{width:1200px;height:3333px;overflow:hidden;background:var(--white)}
body{position:relative;font-family:'Roboto',sans-serif;color:var(--ink)}
.abs{position:absolute}

/* header */
.brand{left:140px;top:52px;display:flex;align-items:center;gap:8px}
.brand-dot{width:14px;height:14px;border-radius:50%;background:var(--orange)}
.brand-name{font-family:'Montserrat',sans-serif;font-weight:800;font-size:17px;color:var(--orange);line-height:1.1;width:90px}
.nav-link{top:62px;font-size:16px;color:var(--grey-text);letter-spacing:.3px}
.pill{display:flex;align-items:center;justify-content:center;background:var(--orange);color:var(--white);font-family:'Montserrat',sans-serif;font-weight:700;border-radius:40px}
.btn-signup{left:833px;top:50px;width:131px;height:43px;font-size:16px}
.btn-register{left:991px;top:50px;width:131px;height:43px;font-size:16px}

/* hero */
.hero{left:0;top:136px;width:1200px;height:470px;background:var(--band);border-radius:8px}
.hero-title{left:140px;top:214px;font-family:'Montserrat',sans-serif;font-weight:700;font-size:41px;color:#4a4a4a;letter-spacing:1.5px}
.hero-copy{left:141px;top:293px;font-size:21px;line-height:44px;color:#444;letter-spacing:.6px}
.btn-shop{left:140px;top:458px;width:226px;height:75px;font-size:16px;letter-spacing:1px}
.hero-art{left:718px;top:211px;width:391px;height:317px;border-radius:24px;background:linear-gradient(180deg,var(--peach) 0%,#f0b56e 60%,#e08a1e 100%)}

/* products */
.section-title{left:0;width:1200px;top:678px;text-align:center;font-family:'Montserrat',sans-serif;font-weight:900;font-size:54px;color:var(--orange);letter-spacing:2px}
.product{width:260px;text-align:center}
.product-label{font-size:17px;line-height:22px;color:#333}
.product-photo{display:block;width:203px;height:149px;margin:26px 0 0 0;border-radius:18px;background:linear-gradient(135deg,#2c2c2c 0%,#8d8d9a 30%,#dcdce6 55%,#f3f3f7 100%)}
.product-price{margin-top:58px;font-family:'Montserrat',sans-serif;font-weight:800;font-size:34px;color:#333}
.btn-more{left:521px;top:1608px;width:226px;height:74px;font-size:16px;letter-spacing:.5px}

/* testimonial */
.quote-band{left:0;top:1795px;width:1200px;height:481px;background:var(--band)}
.quote-mark{left:0;width:1200px;top:1825px;text-align:center;font-family:'Montserrat',sans-serif;font-weight:900;font-size:120px;line-height:120px;color:#8a8a8a}
.quote-text{left:130px;width:940px;top:1945px;text-align:center;font-size:26px;line-height:33px;font-weight:300;color:#9a9a9a}
.avatar{border-radius:50%;background:radial-gradient(circle at 50% 40%,#9aa2ad,#4a4f57 70%,#2f3338)}
.avatar.faded{opacity:.45}
.person-name{font-family:'Montserrat',sans-serif;font-weight:700}
.person-role{font-size:12px}
.arrow{width:20px;height:32px}

/* newsletter */
.news-photo{left:140px;top:2387px;width:490px;height:490px;background:linear-gradient(160deg,#2a2622 0%,#4a3a2e 55%,#5b4433 100%)}
.news-title{left:140px;top:2578px;width:490px;text-align:center;font-family:'Montserrat',sans-serif;font-weight:900;font-size:58px;line-height:56px;color:var(--white)}
.news-panel{left:630px;top:2387px;width:492px;height:490px;background:var(--band)}
.email{left:709px;top:2530px;width:335px;height:67px;border:1px solid #b5b5b5;border-radius:8px;background:var(--white);padding:0 20px;display:flex;align-items:center;font-size:16px;color:#a5a5a5}
.btn-news{left:711px;top:2621px;width:333px;height:109px;border-radius:26px;font-size:25px;line-height:26px;text-align:center;letter-spacing:1px}

/* footer */
.footer{left:0;top:2988px;width:1200px;height:345px;background:var(--footer)}
.foot-col{top:3088px;color:var(--white)}
.foot-col h4{font-family:'Montserrat',sans-serif;font-weight:800;font-size:17px;letter-spacing:.5px;margin-bottom:12px}
.foot-col li{list-style:none;font-size:14px;font-weight:500;line-height:29px}
.foot-brand{left:1000px;top:3140px;display:flex;align-items:center;gap:8px}
.foot-brand .brand-name{font-size:24px;width:auto;text-align:right}
</style>
</head>
<body>

<header>
  <div class="abs brand"><span class="brand-dot"></span><span class="brand-name">Falcrest Trail</span></div>
  <a class="abs nav-link" style="left:260px">Products</a>
  <a class="abs nav-link" style="left:377px">Today’s Deals</a>
  <a class="abs nav-link" style="left:531px">Customer Services</a>
  <a class="abs nav-link" style="left:723px">Contact</a>
  <a class="abs pill btn-signup">Sign up</a>
  <a class="abs pill btn-register">Register</a>
</header>

<section>
  <div class="abs hero"></div>
  <h1 class="abs hero-title">Falcrest Trail</h1>
  <p class="abs hero-copy">Offers you all you need to go fishing.<br>With Falcrest Trail you can go fishing<br>with all the equipments you need!</p>
  <a class="abs pill btn-shop">SHOP NOW</a>
  <div class="abs hero-art" role="img" aria-label="Illustration of a person fishing from an orange boat on the water"></div>
</section>

<section>
  <h2 class="abs section-title">Products</h2>

  <div class="abs product" style="left:120px;top:862px"><p class="product-label">Top seller’s in<br>‘Glasses’</p><span class="product-photo" role="img" aria-label="Sports sunglasses with lanyard clip" style="margin-left:20px"></span><p class="product-price">$15.99</p></div>
  <div class="abs product" style="left:487px;top:862px"><p class="product-label">Top seller’s in<br>‘Glasses’</p><span class="product-photo" role="img" aria-label="Sports sunglasses with lanyard clip" style="margin-left:20px"></span><p class="product-price">$9.99</p></div>
  <div class="abs product" style="left:890px;top:862px"><p class="product-label">Top seller’s in<br>‘Glasses’</p><span class="product-photo" role="img" aria-label="Sports sunglasses with lanyard clip" style="margin-left:21px"></span><p class="product-price">$19.99</p></div>

  <div class="abs product" style="left:125px;top:1244px"><p class="product-label">Top seller’s in<br>‘Glasses’</p><span class="product-photo" role="img" aria-label="Sports sunglasses with lanyard clip" style="margin-left:19px"></span><p class="product-price">$2.99</p></div>
  <div class="abs product" style="left:493px;top:1244px"><p class="product-label">Top seller’s in<br>‘Glasses’</p><span class="product-photo" role="img" aria-label="Sports sunglasses with lanyard clip" style="margin-left:20px"></span><p class="product-price">$29.99</p></div>
  <div class="abs product" style="left:890px;top:1244px"><p class="product-label">Top seller’s in<br>‘Glasses’</p><span class="product-photo" role="img" aria-label="Sports sunglasses with lanyard clip" style="margin-left:21px"></span><p class="product-price">4.99</p></div>

  <a class="abs pill btn-more">See more!</a>
</section>

<section>
  <div class="abs quote-band"></div>
  <div class="abs quote-mark">“</div>
  <p class="abs quote-text">Lorem ipsum dolor sit amet, consectetur adipiscing elit. Proin non euismod orci. Maecenas rhoncus neque non odio porttitor interdum. Vivamus vehicula quis metus quis facilisis. Sed fringilla at est non ullamcorper</p>

  <svg class="abs arrow" style="left:141px;top:2154px" viewBox="0 0 20 32"><path d="M16 3L5 16L16 29" fill="none" stroke="var(--orange)" stroke-width="5" stroke-linecap="round" stroke-linejoin="round"/></svg>
  <svg class="abs arrow" style="left:1100px;top:2154px" viewBox="0 0 20 32"><path d="M4 3L15 16L4 29" fill="none" stroke="var(--orange)" stroke-width="5" stroke-linecap="round" stroke-linejoin="round"/></svg>

  <span class="abs avatar faded" role="img" aria-label="Portrait photo of a customer" style="left:181px;top:2118px;width:104px;height:104px"></span>
  <div class="abs" style="left:307px;top:2156px;color:#b0b0b0"><p class="person-name" style="font-size:15px">Toren Ashby</p><p class="person-role" style="font-size:10px">Professional Coder</p></div>

  <span class="abs avatar" role="img" aria-label="Portrait photo of a customer" style="left:452px;top:2098px;width:144px;height:144px"></span>
  <div class="abs" style="left:632px;top:2148px;color:#333"><p class="person-name" style="font-size:22px">Toren Ashby</p><p class="person-role" style="font-size:14px;margin-top:2px">Professional Coder</p></div>

  <span class="abs avatar faded" role="img" aria-label="Portrait photo of a customer" style="left:823px;top:2118px;width:104px;height:104px"></span>
  <div class="abs" style="left:959px;top:2156px;color:#b0b0b0"><p class="person-name" style="font-size:15px">Toren Ashby</p><p class="person-role" style="font-size:10px">Professional Coder</p></div>
</section>

<section>
  <div class="abs news-photo" role="img" aria-label="Photo of a hand writing in a notebook on a wooden desk"></div>
  <h2 class="abs news-title">Join our<br>newsletter</h2>
  <div class="abs news-panel"></div>
  <div class="abs email">Email...</div>
  <a class="abs pill btn-news">Sign up for our<br>newsletter</a>
</section>

<footer>
  <div class="abs footer"></div>
  <div class="abs foot-col" style="left:140px"><h4>Get to Know Us</h4><ul><li>About Falcrest Trail</li><li>Career</li><li>Blogs</li><li>Our Developers</li></ul></div>
  <div class="abs foot-col" style="left:339px"><h4>Get to Know Us</h4><ul><li>About Falcrest Trail</li><li>Career</li><li>Blogs</li><li>Our Developers</li></ul></div>
  <div class="abs foot-col" style="left:553px"><h4>Get to Know Us</h4><ul><li>About Falcrest Trail</li><li>Career</li><li>Blogs</li><li>Our Developers</li></ul></div>
  <div class="abs foot-col" style="left:752px"><h4>Get to Know Us</h4><ul><li>About Falcrest Trail</li><li>Career</li><li>Blogs</li><li>Our Developers</li></ul></div>
  <div class="abs foot-brand"><span class="brand-name">Falcrest<br>Trail</span></div>
</footer>

</body>
</html>
```